Agriculture Business Card

I want to use my existing logo and use my tagline of "Don't Guess...Soil Test" on the card. Looking for a double sided card that will really get peoples attention.
Contact Info:
Marlow Field Crop Partners
Calvin Brusk
2716 K Lane
Otoe, NE 68592
402-555-0143
calvin.r.brusk@fieldmailbox.net

```html
<!DOCTYPE html>
<html lang="en">
<head>
<meta charset="utf-8">
<title>Marlow Field Crop Partners – Business Card</title>
<link href="https://fonts.googleapis.com/css2?family=Arimo:wght@400;700&display=swap" rel="stylesheet">
<style>
  :root {
    --backdrop: #2b2c2f;
    --card-green: #35a83f;
    --card-black: #1d1d1f;
    --accent-gold: #f5b51e;
    --brand-brown: #a8684a;
    --text-white: #f4f4f4;
  }
  * { box-sizing: border-box; margin: 0; padding: 0; }
  html, body {
    width: 1200px;
    height: 900px;
    overflow: hidden;
    background: var(--backdrop);
    font-family: "Arimo", Arial, sans-serif;
  }
  .canvas {
    width: 1200px;
    height: 900px;
    display: flex;
    justify-content: center;
    align-items: center;
    gap: 90px;
  }
  .card {
    width: 400px;
    height: 640px;
    background: var(--card-green);
    padding: 16px;
    box-shadow: 0 18px 40px rgba(0,0,0,0.45);
  }
  .card-face {
    width: 100%;
    height: 100%;
    background: var(--card-black);
    display: flex;
    flex-direction: column;
    align-items: center;
    color: var(--text-white);
    text-align: center;
  }
  .brand-mark {
    display: flex;
    flex-direction: column;
    align-items: center;
    gap: 14px;
  }
  .brand-dot {
    width: 84px;
    height: 84px;
    border-radius: 50%;
    background: var(--accent-gold);
  }
  .brand-name {
    font-weight: 700;
    line-height: 1.15;
  }

  /* Front */
  .card-front .card-face { padding-top: 120px; }
  .card-front .brand-name { color: var(--accent-gold); font-size: 18px; width: 200px; }
  .holder-name {
    margin-top: 36px;
    color: var(--accent-gold);
    font-weight: 700;
    font-size: 32px;
    letter-spacing: 0.5px;
  }
  .holder-title {
    margin-top: 4px;
    font-size: 17px;
  }
  .contact-icons {
    display: flex;
    gap: 8px;
    margin-top: 22px;
  }
  .contact-icon {
    width: 30px;
    height: 30px;
  }
  .contact-list {
    list-style: none;
    margin-top: 20px;
    font-size: 16px;
    line-height: 1.55;
  }

  /* Back */
  .card-back .card-face { padding-top: 170px; }
  .card-back .brand-name { color: var(--brand-brown); font-size: 30px; width: 260px; }
  .tagline {
    margin-top: auto;
    margin-bottom: 70px;
    font-size: 24px;
  }
</style>
</head>
<body>
<main class="canvas">

  <section class="card card-front" aria-label="Business card front">
    <div class="card-face">
      <div class="brand-mark">
        <span class="brand-dot" aria-hidden="true"></span>
        <span class="brand-name">Marlow Field Crop Partners</span>
      </div>
      <h1 class="holder-name">CALVIN BRUSK</h1>
      <p class="holder-title">CEO/Founder</p>

      <div class="contact-icons" aria-hidden="true">
        <svg class="contact-icon" viewBox="0 0 30 30">
          <circle cx="15" cy="15" r="13" fill="none" stroke="#f5b51e" stroke-width="2"/>
          <path d="M10 9c1-1 2-1 2.5 0l1.2 2.4c.3.6 0 1.1-.5 1.5l-.8.6c.7 1.6 1.9 2.8 3.5 3.5l.6-.8c.4-.5.9-.8 1.5-.5l2.4 1.2c1 .5 1 1.5 0 2.5-1.2 1.2-3 1.4-5 .3-2.6-1.4-4.6-3.4-6-6-1.1-2-.9-3.8.3-5z" fill="#f5b51e"/>
        </svg>
        <svg class="contact-icon" viewBox="0 0 30 30">
          <circle cx="15" cy="15" r="13" fill="none" stroke="#f5b51e" stroke-width="2"/>
          <rect x="8" y="10" width="14" height="10" rx="1" fill="#f5b51e"/>
          <path d="M8.5 10.5 15 15.5l6.5-5" fill="none" stroke="#1d1d1f" stroke-width="1.3"/>
        </svg>
        <svg class="contact-icon" viewBox="0 0 30 30">
          <circle cx="15" cy="15" r="13" fill="none" stroke="#f5b51e" stroke-width="2"/>
          <path d="M15 7a5 5 0 0 0-5 5c0 3.8 5 10 5 10s5-6.2 5-10a5 5 0 0 0-5-5z" fill="#f5b51e"/>
          <circle cx="15" cy="12" r="2" fill="#1d1d1f"/>
        </svg>
      </div>

      <ul class="contact-list">
        <li>402-555-0143</li>
        <li>calvin.r.brusk@fieldmailbox.net</li>
        <li>2716 K Lane Otoe, NE 68592</li>
      </ul>
    </div>
  </section>

  <section class="card card-back" aria-label="Business card back">
    <div class="card-face">
      <div class="brand-mark">
        <span class="brand-dot" aria-hidden="true"></span>
        <span class="brand-name">Marlow Field Crop Partners</span>
      </div>
      <p class="tagline">Don't Guess...Soil Test</p>
    </div>
  </section>

</main>
</body>
</html>
```